Website for a Psychologist in Private Practice

I need a cool web design for my website: www.drvalporte.com. I would like it to look professional. Keep all the current content and add: Space for video; radio spots (see Silver Harbor Tunes Logo below for those); Quick Inquiry; Chatterbook link; 5 star rating on Rivo; a map; reviews from former patients. I am open to suggestions.

Target Market(s)

Those seeking individual and marital counseling.

Industry/Entity Type

Mental Health

Number of Pages Required

1 page

Font styles to use
Sans Serif
Other font styles liked:
• I'm open but no hard to read script

Requirements
Must have
• All the content on my home page with link for video and radio spots. List services and degrees and expertices (pics not necessary).
Nice to have
• A video of me and radio conversations (logo of Silver Harbor Tunes radio attached).
Should not have
• Cartoons, comedy, etc.... I don't need pictures of services (marital, depression, etc...) Just list those.

```html
<!DOCTYPE html>
<html lang="en">
<head>
<meta charset="utf-8">
<title>Dr. Mara L. Valporte – Psychologist</title>
<link href="https://fonts.googleapis.com/css2?family=Barlow:wght@400;500&family=Tinos:ital@0;1&family=Arimo:ital,wght@0,400;0,700;1,400;1,700&display=swap" rel="stylesheet">
<style>
:root{
  --blue:#2f86c6;
  --blue-dark:#1f6fae;
  --ink:#2b2b2b;
  --body:#444;
  --rule:#cfcfcf;
  --light:#f1f1f1;
  --footer:#231f20;
  --white:#fff;
  --hero-top:#6f9fc9;
  --hero-bottom:#9dbfd8;
}
*{box-sizing:border-box;margin:0;padding:0}
html,body{width:744px;height:1200px;overflow:hidden}
body{position:relative;background:var(--white);font-family:"Arimo",sans-serif;color:var(--body)}
.abs{position:absolute}
.display{font-family:"Barlow",sans-serif;font-weight:400}
.serif{font-family:"Tinos",serif}

/* hero */
.hero-bg{left:0;top:0;width:744px;height:376px;background:linear-gradient(180deg,var(--hero-top) 0%,var(--hero-bottom) 100%)}
.topbar{left:82px;top:0;width:580px;height:58px;background:rgba(20,40,60,.4)}
.site-name{left:90px;top:18px;font-size:24px;color:var(--white);font-weight:500}
.license{left:440px;top:34px;font-size:10px;color:var(--white);font-family:"Barlow",sans-serif}
.call-label{left:577px;top:19px;font-size:9.5px;color:var(--white)}
.call-number{left:579px;top:31px;font-size:13.5px;color:var(--white)}
.nav{left:82px;top:58px;width:580px;height:28px;background:var(--blue);display:flex;align-items:center}
.nav a{font-family:"Barlow",sans-serif;color:var(--white);text-decoration:none;font-size:10.5px;padding:0 10px;height:28px;line-height:28px;border-right:1px solid rgba(255,255,255,.25)}
.nav a.active{background:#dfe9f3;color:var(--ink)}
.follow{left:558px;top:58px;height:28px;display:flex;align-items:center;gap:4px;font-size:7.5px;color:var(--white);font-family:"Barlow",sans-serif}
.follow .dot{width:7px;height:7px;border-radius:50%;background:var(--white)}
.slide{left:82px;top:86px;width:580px;height:272px;background:linear-gradient(180deg,#8cb6dc 0%,#a9c6de 100%);box-shadow:0 8px 10px rgba(0,0,0,.35)}
.slide-title{left:120px;top:184px;font-size:20px;color:var(--ink)}
.slide-tag{left:121px;top:210px;font-size:14px;color:var(--ink);line-height:21px}
.arrow{top:210px;width:23px;height:21px;background:#2b2b2b;border:1px solid #fff;display:flex;align-items:center;justify-content:center}

/* columns */
.col-head{font-size:14px;color:var(--ink);font-family:"Barlow",sans-serif;font-weight:400}
.col-rule{height:2px;background:var(--rule)}
.col-rule::before{content:"";display:block;width:60px;height:2px;background:var(--blue)}
.bio-text{left:83px;top:424px;width:172px;font-size:8.6px;line-height:13px;text-align:justify;color:#555}
.link{font-size:8.6px;color:var(--ink);text-decoration:underline;font-family:"Barlow",sans-serif}
.portrait{border-radius:50%;background:radial-gradient(circle at 50% 40%,#d8c69a 0%,#a88f5c 45%,#3c5a78 100%)}
.expert-name{left:358px;top:434px;font-size:14px;line-height:18px;color:var(--ink)}
.expert-list{left:290px;top:488px;list-style:none;font-size:8.4px;line-height:13px;color:#555}
.expert-list li{display:flex;align-items:center;gap:4px}
.quote-box{left:481px;top:428px;width:176px;height:104px;border:1px solid #ccc;border-radius:3px;box-shadow:0 1px 3px rgba(0,0,0,.15);background:#fafafa;padding:7px 9px}
.quote-box p{font-size:8.4px;line-height:13px;color:#333;text-indent:14px}
.quote-mark{left:490px;top:430px;font-size:16px;color:#aaa;font-family:"Tinos",serif}
.quote-by{left:612px;top:512px;font-size:7.6px;color:#555;font-family:"Tinos",serif}

/* degrees */
.degrees{left:81px;top:579px;width:581px;height:48px;background:var(--blue)}
.degrees-title{left:148px;top:595px;font-size:14px;color:var(--white)}
.degree{font-size:8.4px;color:var(--white);font-family:"Barlow",sans-serif}

/* media row */
.video{left:88px;top:678px;width:182px;height:138px;border:2px solid var(--blue);background:linear-gradient(160deg,#5b6a48 0%,#a89a72 50%,#5a6740 100%)}
.form-intro{left:295px;top:681px;font-size:7.2px;color:#333}
.field{left:293px;width:173px;height:19px;border:1px solid #ccc;background:var(--white);font-size:7.2px;color:#666;padding:5px 6px}
.submit{left:293px;top:797px;width:69px;height:19px;background:var(--blue);color:var(--white);font-size:9px;font-weight:700;display:flex;align-items:center;justify-content:center}
.radio-poster{left:486px;top:652px;width:163px;height:163px;background:linear-gradient(160deg,#d5254f 0%,#a66a63 50%,#c3204a 100%)}

/* reviews */
.reviews{left:0;top:841px;width:744px;height:181px;background:var(--light)}
.reviews-title{left:0;top:860px;width:744px;text-align:center;font-size:14px;color:var(--ink)}
.reviews-rule{left:278px;top:881px;width:188px;height:1px;background:#bbb}
.reviews-rule::before{content:"";position:absolute;left:72px;top:-1px;width:45px;height:2px;background:var(--blue)}
.review-photo{left:88px;top:898px;width:72px;height:72px;border-radius:50%;background:radial-gradient(circle at 50% 40%,#c9a98a 0%,#6e5a4a 50%,#2a3038 100%);border:2px solid #fff;box-shadow:0 1px 3px rgba(0,0,0,.3)}
.review-text{left:172px;top:902px;width:478px;font-size:8px;line-height:14.6px;font-style:italic;color:#222;text-indent:22px}
.review-by{left:174px;top:969px;font-size:7.9px;font-style:italic;font-weight:700;color:#333}
.more-reviews{left:563px;top:981px;font-size:8px;color:#555}
.more-reviews span{text-decoration:underline}

/* footer */
.footer{left:0;top:1022px;width:744px;height:152px;background:var(--footer)}
.foot-head{font-size:8.8px;color:var(--white);padding-bottom:5px;border-bottom:1px dashed #666}
.foot-links{left:90px;top:1063px;list-style:none;font-size:7.8px;line-height:13.8px;color:var(--white)}
.foot-links li:first-child{color:#c9a46d}
.badge{left:212px;width:128px;border:2px solid var(--blue)}
.contact{font-size:7.8px;color:var(--white);line-height:11.5px}
.rivo-badge{left:595px;top:1058px;width:50px;height:50px;border-radius:6px;background:#c5282b;box-shadow:0 1px 2px rgba(0,0,0,.5)}
.share{left:592px;top:1120px;width:57px;height:19px;background:#3f5f9c;border-radius:2px;display:flex;align-items:center;justify-content:center;gap:4px;color:var(--white);font-size:7.5px}
.share i{display:block;width:8px;height:8px;background:var(--white)}
.copyright{left:0;top:1174px;width:744px;height:26px;background:var(--blue);color:var(--white);font-size:7.8px;text-align:center;line-height:26px}
</style>
</head>
<body>

<!-- hero -->
<div class="abs hero-bg" role="img" aria-label="Beach background photo"></div>
<div class="abs topbar"></div>
<div class="abs site-name display">Dr. Mara L. Valporte</div>
<div class="abs license">California # PSY20581</div>
<svg class="abs" style="left:553px;top:22px" width="19" height="19" viewBox="0 0 19 19" aria-hidden="true">
  <circle cx="9.5" cy="9.5" r="8.5" fill="none" stroke="#fff" stroke-width="1"/>
  <path d="M7 5c-1 1-1 3 .5 5.5S11 14 12.5 13.5l1-1-1.8-1.5-1 .6C10 11 8.6 9.6 8.2 8.7l.6-1L7.6 5.5z" fill="#fff"/>
</svg>
<div class="abs call-label">Call Us Today</div>
<div class="abs call-number">555-310-4826</div>

<nav class="abs nav">
  <a class="active" href="#">Home</a>
  <a href="#">About Me</a>
  <a href="#">Sessions</a>
  <a href="#">Resources</a>
  <a href="#">BIO</a>
  <a href="#">Customer Reviews</a>
  <a href="#" style="border-right:none">Contact Us</a>
</nav>
<div class="abs follow"><span class="dot"></span>Chatterbook <span class="dot"></span>Tweetline</div>

<div class="abs slide" role="img" aria-label="Slide photo: woman with arms outstretched by the sea"></div>
<div class="abs slide-title display">Dr. Mara L. Valporte</div>
<div class="abs slide-tag display">The Best way to Conquer a<br>problem is to FACE it</div>
<div class="abs arrow" style="left:86px"><svg width="8" height="10" viewBox="0 0 8 10"><path d="M6 1 2 5l4 4" fill="none" stroke="#fff" stroke-width="2"/></svg></div>
<div class="abs arrow" style="left:634px"><svg width="8" height="10" viewBox="0 0 8 10"><path d="M2 1l4 4-4 4" fill="none" stroke="#fff" stroke-width="2"/></svg></div>

<!-- biography -->
<h2 class="abs col-head" style="left:83px;top:393px">My Biography</h2>
<div class="abs col-rule" style="left:83px;top:414px;width:172px"></div>
<p class="abs bio-text serif">While I acknowledge the importance of my education, I also appreciate the role my experiences have played in allowing me to relate so well to others. Allow me to share those I feel are most relevant with you. I survived an abusive childhood that my mother &amp; sister unfortunately did not. &amp; it was my grief &amp; desire to become stronger than my past that led me to counseling.....</p>
<a class="abs link" style="left:83px;top:546px" href="#">Read More</a>

<!-- expertise -->
<h2 class="abs col-head" style="left:289px;top:392px">My Expertise</h2>
<div class="abs col-rule" style="left:289px;top:414px;width:173px"></div>
<div class="abs portrait" style="left:287px;top:424px;width:61px;height:61px" role="img" aria-label="Portrait of Dr. Valporte"></div>
<div class="abs expert-name display">Dr. Mara L.<br>Valporte</div>
<ul class="abs expert-list serif">
  <li><svg width="8" height="7" viewBox="0 0 8 7"><path d="M1 4l2 2 4-5" fill="none" stroke="#2f86c6" stroke-width="1.6"/></svg>Dating, Marriage,</li>
  <li><svg width="8" height="7" viewBox="0 0 8 7"><path d="M1 4l2 2 4-5" fill="none" stroke="#2f86c6" stroke-width="1.6"/></svg>Parenting &amp; Professional Relationships</li>
  <li><svg width="8" height="7" viewBox="0 0 8 7"><path d="M1 4l2 2 4-5" fill="none" stroke="#2f86c6" stroke-width="1.6"/></svg>Depression &amp; Anxiety Issues</li>
  <li><svg width="8" height="7" viewBox="0 0 8 7"><path d="M1 4l2 2 4-5" fill="none" stroke="#2f86c6" stroke-width="1.6"/></svg>Personality Disorders</li>
  <li><svg width="8" height="7" viewBox="0 0 8 7"><path d="M1 4l2 2 4-5" fill="none" stroke="#2f86c6" stroke-width="1.6"/></svg>Life Management</li>
</ul>

<!-- radio -->
<h2 class="abs col-head" style="left:482px;top:393px">Radio Conversations</h2>
<div class="abs col-rule" style="left:482px;top:414px;width:173px"></div>
<div class="abs quote-box"><p>Lorem ipsum dolor sit ae onsectetuer adipiscing elit, sed diam nonummy nibh euis tincidunt ut laoreetlore gna aliquam erat olutpat. Ut wisi enim adinim veniam, quis strud xerci tation ullamrper suscipit lobortis sl ut al lorem.</p></div>
<div class="abs quote-mark">&ldquo;</div>
<div class="abs quote-by">Anna Reyes</div>
<a class="abs link" style="left:482px;top:540px" href="#">View All</a>

<!-- degrees -->
<div class="abs degrees"></div>
<div class="abs degrees-title display">My Degrees</div>
<svg class="abs" style="left:228px;top:587px" width="12" height="35" viewBox="0 0 12 35" aria-hidden="true">
  <path d="M2 1c5 0 5 2 5 7v5c0 3 1 4 4 4.5-3 .5-4 1.5-4 4.5v5c0 5 0 7-5 7" fill="none" stroke="#a9cdea" stroke-width="1.2"/>
</svg>
<div class="abs degree" style="left:252px;top:590px">Doctoral Degree in Clinical Psychology</div>
<div class="abs degree" style="left:252px;top:607px">Masters Degree in Counseling Psychology</div>
<div class="abs degree" style="left:442px;top:590px">Doctoral Internship, Lakeside Medical Center</div>
<div class="abs degree" style="left:442px;top:607px">Masters Internship, Harborview Clinic</div>

<!-- video -->
<h2 class="abs col-head" style="left:88px;top:649px">View Video</h2>
<div class="abs col-rule" style="left:88px;top:669px;width:182px"></div>
<div class="abs video" role="img" aria-label="Video introduction from Dr. Valporte"></div>
<svg class="abs" style="left:159px;top:736px" width="20" height="20" viewBox="0 0 20 20" aria-hidden="true">
  <circle cx="10" cy="10" r="8.5" fill="none" stroke="#fff" stroke-width="1.5" opacity=".85"/>
  <path d="M8 6l6 4-6 4z" fill="#fff" opacity=".85"/>
</svg>

<!-- inquiry -->
<h2 class="abs col-head" style="left:293px;top:649px">Quick Inquiry</h2>
<div class="abs col-rule" style="left:293px;top:669px;width:173px"></div>
<div class="abs form-intro">Lorem ipsum dolor sit amet, consectetuer</div>
<div class="abs field" style="top:695px">Name</div>
<div class="abs field" style="top:717px">Email</div>
<div class="abs field" style="top:740px">Phone</div>
<div class="abs field" style="top:762px;height:31px">Message</div>
<div class="abs submit">SUBMIT</div>

<!-- radio show -->
<div class="abs radio-poster" role="img" aria-label="Silver Harbor Tunes radio show poster, Sundays 4pm PST"></div>

<!-- reviews -->
<div class="abs reviews"></div>
<h2 class="abs reviews-title display">Reviews From Former Patients</h2>
<div class="abs reviews-rule"></div>
<div class="abs review-photo" role="img" aria-label="Portrait of a former patient"></div>
<p class="abs review-text">Lorem ipsum dolor sit amet, consectetuer adipiscing elit, sed diam nonummy nibh euismod tincidunt ut laoreet dolore magna aliquam erat volutpat. Ut wisi enim ad minim veniam, quis nostrud exerci tation ullamcorper suscipit lobortis nisl ut aliquip commodo consequat. Duis autem vel eum iriure dolor in hendrerit in vulputate velit esse molestie consequat, vel illum dolore eu feugiat nulla facilisis at vero eros et accumsan et iusto odio dignissimaugue duis dolore te feugait nulla facilisi.</p>
<div class="abs review-by">.... Lorem Ispum, Manger</div>
<div class="abs more-reviews"><span>Read more testimonials</span> &raquo;</div>

<!-- footer -->
<footer class="abs footer"></footer>
<div class="abs foot-head" style="left:90px;top:1039px;width:73px">Quick Links</div>
<ul class="abs foot-links">
  <li>Home</li><li>About Me</li><li>Sessions</li><li>Resources</li><li>BIO</li><li>Customer Reviews</li><li>Contact Me</li>
</ul>
<div class="abs foot-head" style="left:212px;top:1039px;width:158px">A Portion of All Revenue Is Donated To</div>
<div class="abs badge" style="top:1061px;height:49px;background:#fff" role="img" aria-label="Children's advocacy partner badge"></div>
<div class="abs badge" style="top:1114px;height:48px;background:#8fa73c" role="img" aria-label="Family services partner badge"></div>
<div class="abs foot-head" style="left:423px;top:1039px;width:118px">Contact Details</div>
<div class="abs contact" style="left:423px;top:1064px">A:</div>
<div class="abs contact" style="left:441px;top:1064px">410 Harbor Lane, Suite 120<br>Bayview, CA 90000</div>
<div class="abs contact" style="left:423px;top:1099px">P:&nbsp;&nbsp;&nbsp;&nbsp;555-310-4826</div>
<div class="abs contact" style="left:423px;top:1120px">TF:&nbsp;&nbsp;&nbsp;555-310-4826</div>
<div class="abs contact" style="left:423px;top:1141px">E:&nbsp;&nbsp;&nbsp;&nbsp;mv@drvalporte.com</div>
<div class="abs rivo-badge" role="img" aria-label="Rivo customer reviews badge"></div>
<div class="abs share"><i></i>SHARE</div>

<div class="abs copyright">Copyright &copy; 2016 Dr. Mara L. Valporte&nbsp; All rights reserved</div>

</body>
</html>
```